Pebble nook day nursery qrv limited

we would like create a website that can be updated by us easily as we have regular changes to what we provide and need. we would like something that is classy but also appealing from a child's aspect. we would be looking to add our own logo and our edvarin logo both attached, if you guys can create it and we will work with the preferred choice to add all the text.
We would like the links to kin pathways, edvarin report and our chatterloom feed on the front page

we are looking for a website for our childcare business we have 2 nurseries that we would like one website.
showing our opening hours, price list, policies etc as well as photos, description of our day, staff photos and their training accreditation's.

Target Market(s)

Families

Industry/Entity Type

Childcare

Number of Pages Required

5+ page

Font styles to use
Serif

Colors

Designer to choose colors to be used in the design.

Requirements
Must have
• links to social media and other websites, photographs, links to download registration forms etc, parents able to leave reviews. wayrund plots link, job opportunities
Nice to have
• facilities to take payments

```html
<!DOCTYPE html>
<html lang="en">
<head>
<meta charset="utf-8">
<title>Pebble nook day nursery qrv limited</title>
<link rel="stylesheet" href="https://fonts.googleapis.com/css2?family=Source+Serif+4:opsz,wght@8..60,400;8..60,600;8..60,700&display=swap">
<style>
  :root {
    --page-bg: #f4f4f4;
    --ink: #1f1f1f;
    --white: #ffffff;
    --accent-orange: #f3a523;
    --accent-green: #8a9a2e;
    --features-top: #55473a;
    --features-mid: #3f352b;
    --features-bottom: #2e261f;
    --vision-left: #3f4c2a;
    --vision-mid: #56623a;
    --vision-shade: #263044;
  }
  * { margin: 0; padding: 0; box-sizing: border-box; }
  html, body { width: 866px; height: 1200px; overflow: hidden; }
  body {
    background: var(--page-bg);
    font-family: "Source Serif 4", Georgia, serif;
    color: var(--ink);
    position: relative;
  }
  .section { position: absolute; left: 0; width: 866px; }
  .photo-fill { position: absolute; inset: 0; }

  .features { top: 0; height: 456px; }
  .features .photo-fill {
    background:
      radial-gradient(ellipse 260px 200px at 230px 230px, rgba(130,105,80,.45), transparent 70%),
      radial-gradient(ellipse 240px 220px at 620px 220px, rgba(140,115,90,.4), transparent 70%),
      linear-gradient(180deg, var(--features-top) 0%, var(--features-mid) 60%, var(--features-bottom) 100%);
  }
  .section-title {
    position: absolute; left: 0; width: 100%;
    text-align: center;
    font-weight: 700;
    font-size: 22px;
    line-height: 26px;
  }
  .features .section-title { top: 48px; color: var(--white); }
  .feature { position: absolute; top: 104px; width: 118px; color: var(--white); }
  .feature-title {
    font-weight: 600;
    font-size: 16px;
    line-height: 20px;
    color: var(--accent-orange);
    text-align: center;
    margin-bottom: 19px;
    white-space: nowrap;
  }
  .feature-text {
    font-size: 8.4px;
    line-height: 10.9px;
    text-align: justify;
    text-shadow: 0 0 2px rgba(0,0,0,.6);
  }
  .feature.one { left: 222px; }
  .feature.two { left: 377px; }
  .feature.three { left: 527px; }

  .why { top: 456px; height: 350px; background: var(--page-bg); }
  .why .section-title { top: 30px; color: var(--accent-green); }
  .prose {
    position: absolute; left: 223px; width: 420px;
    font-size: 10.6px;
    line-height: 16.2px;
    text-align: justify;
  }
  .why .prose { top: 80px; color: var(--ink); }

  .vision { top: 806px; height: 382px; }
  .vision .photo-fill {
    background:
      radial-gradient(ellipse 220px 240px at 700px 260px, rgba(38,48,68,.85), transparent 75%),
      radial-gradient(ellipse 200px 200px at 150px 250px, rgba(110,120,80,.4), transparent 70%),
      linear-gradient(90deg, var(--vision-left) 0%, var(--vision-mid) 50%, var(--vision-left) 100%);
  }
  .vision .section-title { top: 32px; color: var(--white); }
  .vision .prose { top: 84px; color: var(--white); text-shadow: 0 0 2px rgba(0,0,0,.5); }
</style>
</head>
<body>

<section class="section features">
  <div class="photo-fill" role="img" aria-label="Photo of two children peeking over autumn leaves, warm dimmed tones"></div>
  <h2 class="section-title">OUR FEATURES</h2>
  <div class="feature one">
    <h3 class="feature-title">Play &amp; explore</h3>
    <p class="feature-text">Our rooms are bright, warm and full of things to touch, build and explore. Each day mixes free play with gentle group time, songs and stories, so little ones settle quickly and grow in confidence. Fresh snacks, quiet corners for naps and a secure garden with sand, water and planting beds make both of our nurseries feel like a second home for babies, toddlers and preschoolers alike, every single day of the week.</p>
  </div>
  <div class="feature two">
    <h3 class="feature-title">Early learning</h3>
    <p class="feature-text">We follow each child's interests and plan small next steps for speaking, counting, drawing and sharing. Preschoolers enjoy letter sounds, number games and little projects that get them ready for school. Families receive regular updates, photos and learning notes, and our latest edvarin report can be read from the home page. Every room keeps a shelf of picture books that children can take home and share with the people they love most.</p>
  </div>
  <div class="feature three">
    <h3 class="feature-title">Caring staff</h3>
    <p class="feature-text">Every child has a key worker who knows their routines, favourite toys and little worries. Our team holds first aid, safeguarding and early years qualifications, and training continues all year round. Staff photos and accreditations sit on our team page, and we are always happy to talk at pickup. We are proud that many of our practitioners have been with us for years and have grown alongside the families they support.</p>
  </div>
</section>

<section class="section why">
  <h2 class="section-title">WHY CHOOSE US ?</h2>
  <div class="prose">
    <p>Pebble nook day nursery qrv limited runs two friendly nurseries under one caring team. We open early and close late so working families have time to spare, and our price list, opening hours and policies are always clear and easy to find. Children spend their days playing, painting, singing and exploring outdoors, guided by practitioners who truly know them. Registration forms can be downloaded in a moment, and parents are warmly invited to leave reviews and tell us how we can do even better.</p>
    <p>Our settings are safe, bright and thoughtfully planned, with separate spaces for babies, toddlers and preschoolers. Home cooked meals are prepared fresh on site each day, allergies are handled with great care, and nap times follow each family's routine. You can follow our chatterloom feed for daily snapshots, find each nursery on wayrund plots and read about funded places on kin pathways. We are also growing our team, so keep an eye on job opportunities if you love working with young children.</p>
  </div>
</section>

<section class="section vision">
  <div class="photo-fill" role="img" aria-label="Photo of a little girl blowing soap bubbles in a green park, dimmed"></div>
  <h2 class="section-title">OUR VISION</h2>
  <div class="prose">
    <p>We believe early childhood should be full of wonder. Our vision is a nursery where every child feels safe, listened to and free to be curious, where days are filled with laughter, fresh air and small discoveries that build big confidence. We want each little one to leave us kind, capable and excited to learn, ready for school and for the world beyond it. Every plan we make, from room layouts to daily menus, starts with the question of what is best for the children in our care.</p>
    <p>We also see families as true partners. Parents know their children best, so we share updates openly, welcome ideas and make time for honest conversations. Our staff keep learning too, refreshing their training so our care keeps pace with the latest early years thinking. As our two nurseries grow, we hope to stay warm, personal and rooted in our community, a place families recommend to friends and children remember fondly long after their nursery days have ended.</p>
  </div>
</section>

</body>
</html>
```